Brivane - Business Cards for a new venture

create business card for a startup classified business dealing in construction materials, the cards need to have a professional look but modern, more serious than playful, one of the samples must include the official font (attached), please explore using the official colors in the company's logo

Target Market(s)

Energy sector

Contact Information for Business Card

Font styles to use
Other font styles liked:
• suissnord

Requirements
Must have
• corporate colors (in logo attached)
Nice to have
• Official font (in one of the samples) font is : suissnord
Should not have
• Cartoonish look

```html
<!DOCTYPE html>
<html lang="en">
<head>
<meta charset="utf-8">
<title>Brivane – Business Card</title>
<link rel="stylesheet" href="https://fonts.googleapis.com/css2?family=Work+Sans:wght@400;500;600&display=swap">
<style>
  :root{
    --navy:#0b4a86;
    --navy-deep:#083a6b;
    --steel:#8b9096;
    --ink:#3b3f44;
    --paper:#ffffff;
    --paper-shade:#eef0f2;
    --stage:#d9dcdf;
  }
  *{box-sizing:border-box;margin:0;padding:0}
  html,body{width:1200px;height:900px;overflow:hidden}
  body{
    background:var(--stage);
    font-family:"Work Sans",Arial,sans-serif;
    display:flex;flex-direction:column;align-items:center;justify-content:center;gap:60px;
  }
  .card{
    position:relative;width:630px;height:360px;border-radius:22px;overflow:hidden;
    box-shadow:0 10px 30px rgba(0,0,0,.18);
  }
  .card--front{background:linear-gradient(135deg,var(--paper-shade) 0%,var(--paper) 45%,var(--paper) 100%)}
  .card--back{
    background:radial-gradient(ellipse at 40% 30%,#0e5495 0%,var(--navy-deep) 80%);
    display:flex;align-items:center;justify-content:center;
  }
  .brand{
    display:flex;align-items:center;gap:14px;
    font-weight:500;letter-spacing:.22em;text-transform:uppercase;
  }
  .brand__square{width:18px;height:18px;background:var(--navy)}
  .card--front .brand{position:absolute;left:160px;top:78px;font-size:40px;color:var(--steel)}
  .card--back .brand{font-size:52px;color:#c9ccd0}
  .card--back .brand__square{background:#c9ccd0;width:22px;height:22px}
  .divider{position:absolute;left:46px;top:196px;width:500px;height:2px;background:var(--navy);opacity:.75}
  .contact{position:absolute;left:46px;top:214px;list-style:none;font-size:16px;color:var(--ink);line-height:27px}
  .contact li{display:flex;align-items:center;gap:10px}
  .contact svg{width:13px;height:13px;fill:var(--navy)}
  .contact .web{color:var(--navy)}
  .person{position:absolute;right:60px;top:128px;text-align:right}
  .person__name{font-size:27px;font-weight:600;color:var(--navy);letter-spacing:.02em;text-transform:uppercase}
  .person__role{font-size:16px;color:var(--ink);margin-top:2px}
  .accent-bar{position:absolute;right:0;top:150px;width:34px;height:46px;background:var(--navy);border-left:5px solid var(--paper);outline:3px solid var(--navy);outline-offset:-3px}
  .address{position:absolute;right:60px;top:218px;text-align:right;font-size:17px;color:var(--ink);line-height:27px}
</style>
</head>
<body>
  <section class="card card--front">
    <div class="brand"><span class="brand__square"></span>Brivane</div>
    <div class="person">
      <p class="person__name">Adrian Kovel</p>
      <p class="person__role">Director</p>
    </div>
    <div class="accent-bar"></div>
    <div class="divider"></div>
    <ul class="contact">
      <li><svg viewBox="0 0 16 16"><path d="M4 1l3 3-2 2c1 2 3 4 5 5l2-2 3 3-2 3C7 15 1 9 1 3z"/></svg>+330 5187-4206</li>
      <li><svg viewBox="0 0 16 16"><path d="M1 3h14v10H1zM2.5 4.5v.6L8 9l5.5-3.9v-.6zM2.5 6.8V11.5h11V6.8L8 10.7z"/></svg>info@brivane.com</li>
      <li><svg viewBox="0 0 16 16"><circle cx="8" cy="8" r="7"/></svg><span class="web">www.brivane.com</span></li>
    </ul>
    <p class="address">2480 Harlow Street, Unit 4,<br>Eastmere, PO 40718</p>
  </section>
  <section class="card card--back">
    <div class="brand"><span class="brand__square"></span>Brivane</div>
  </section>
</body>
</html>
```